Webdesign für Gerüstbau Wendrich
Zielgruppe
In der über 20-jährigen erfolgreichen Firmengeschichte ist die Firma Gerüstbau Wendrich GmbH ein leistungsstarker und kompetenter Partner für Kunden im Raum Sachsen und Thüringen. Der Aktionsradius erstreckt sich auf ca. 100 km um die Stadt Glauchau OT Talbrunn herum. Das Unternehmen arbeitet ausschließlich mit Kornath-Gerüsten.
Dafür stehen ca. 40.000 m² Kornath-Flink-Gerüst, ca. 4.000 m² Modulgerüst, Kassetten- und Planendächer, Treppenaufgänge und Nottreppen, Fahr- und Rollgerüste sowie weitere Sonderteile zur Verfügung.
Zielgruppe sind:
- Bau- und Dachdeckerfirmen,
- Handwerksbetriebe,
- Ingenieurbüros,
- Kommunen,
- Kirchen,
- landwirtschaftlichen Betriebe,
- Industrie
- und Privatpersonen
Aufgabenstellung
Unserem Auftraggeber gefällt ein großes Auftaktfoto gut, ansonsten ist er offen für ein modernes Layout.
- Layout als PSD
- Notwendige Bilder ausschließlich von Bildfundus.example
- Bitte nur die Startseite layouten
- blau des Logos und eine Zweitfarbe
- Slogan: Wir lösen Ihre Gerüstprobleme! Sprechen Sie mit uns!

```html
<!DOCTYPE html>
<html lang="de">
<head>
<meta charset="utf-8">
<title>Gerüstbau Wendrich – Startseite</title>
<link rel="stylesheet" href="https://fonts.googleapis.com/css2?family=Inter:wght@300;400;500;600;700&display=swap">
<style>
:root{
  --brand:#075a91;
  --tab:#e6edf4;
  --ink:#3a3a3a;
  --white:#ffffff;
  --sky:#bcdcf8;
  --rule:#9a9a9a;
}
*{margin:0;padding:0;box-sizing:border-box}
html,body{width:983px;height:1200px;overflow:hidden;background:var(--white)}
body{position:relative;font-family:'Inter',sans-serif;color:var(--ink)}
.abs{position:absolute}

.hero-band{left:56px;top:140px;width:869px;height:204px;background:var(--brand)}
.brand-mark{left:86px;top:44px;width:151px;height:151px;background:var(--brand);box-shadow:0 2px 6px rgba(0,0,0,.25);display:flex;align-items:center;justify-content:center}
.brand-mark span{color:var(--white);font-weight:600;font-size:15px;text-align:center;line-height:1.25}
.brand-name{left:258px;top:72px;font-weight:700;font-size:30px;line-height:1;color:var(--brand);white-space:nowrap}
.site-title{right:85px;top:50px;text-align:right;color:var(--brand)}
.site-title .name{font-weight:700;font-size:25px;line-height:1}
.site-title .place{font-weight:300;font-size:24px;line-height:1}
.site-title .since{font-weight:400;font-size:14px;margin-top:6px}
.slogan{left:86px;top:213px;color:var(--white);font-weight:300;font-size:25px;line-height:1.22}
.hero-photo{left:567px;top:150px;width:324px;height:183px;border-radius:32px;background:linear-gradient(180deg,#3d7fd6 0%,#5f93d8 45%,#2b4a70 100%)}

.main-nav{left:56px;top:392px;display:flex;gap:10px}
.main-nav a{width:142px;height:40px;display:flex;align-items:center;justify-content:center;background:var(--tab);color:var(--brand);font-size:8.5px;font-weight:600;letter-spacing:.3px;text-decoration:none}
.main-nav a:last-child{width:121px}
.main-nav a.active{background:var(--brand);color:var(--white)}

.history{left:58px;top:473px;width:867px;height:526px;background:var(--brand)}
.history-text{left:93px;top:513px;width:512px;color:var(--white)}
.history-text h2{font-size:15px;font-weight:600;line-height:1.25;margin-bottom:37px}
.history-text p{font-size:10px;line-height:1.25;margin-bottom:22px}
.history-photo{left:614px;top:487px;width:311px;height:465px;background:linear-gradient(180deg,#1f3e78 0%,#8e98a8 40%,#c4c6c4 75%,#8a8570 100%)}

.footer-rule{left:58px;top:1069px;width:867px;height:1px;background:var(--rule)}
.footer-col{top:1088px;font-size:9px;line-height:1.25;color:var(--ink)}
.partner{left:72px;top:1124px;display:flex;align-items:center;gap:10px}
.partner .pname{font-size:20px;font-weight:500;color:#2b2b2b}
.partner .square{width:16px;height:16px;background:var(--brand)}
.partner .claim{font-size:8.5px;color:#555;line-height:1.35}
.badge{left:632px;top:1086px;width:116px;height:59px;background:var(--sky)}
</style>
</head>
<body>
<header>
  <div class="abs hero-band"></div>
  <div class="abs brand-mark"><span>Gerüstbau<br>Wendrich</span></div>
  <div class="abs brand-name">Gerüstbau Wendrich</div>
  <div class="abs site-title">
    <div class="name">Gerüstbau Wendrich</div>
    <div class="place">Talbrunn</div>
    <div class="since">über 30 Jahre Gerüstbau Wendrich 1991-2022</div>
  </div>
  <p class="abs slogan">Wir lösen auch Ihre Gerüstprobleme!<br>Sprechen Sie mit uns!</p>
  <div class="abs hero-photo" role="img" aria-label="Eingerüstetes Mehrfamilienhaus unter blauem Winterhimmel"></div>
</header>

<nav class="abs main-nav">
  <a href="#" class="active">FASSADENGERÜSTE</a>
  <a href="#">AKTUELLES</a>
  <a href="#">UNTERNEHMEN</a>
  <a href="#">STELLENANGEBOTE</a>
  <a href="#">IMPRESSUM</a>
  <a href="#">KONTAKT</a>
</nav>

<main>
  <section class="abs history"></section>
  <div class="abs history-text">
    <h2>Aus der Firmengeschichte der<br>Firma Gerüstbau Wendrich Talbrunn</h2>
    <p>Unsere Firma „Gerüstbau Wendrich“ wurde 1991 vom jetzigen Inhaber, Herrn Jens Wendrich, gegründet.</p>
    <p>In der über 20-jährigen erfolgreichen Firmengeschichte waren und sind wir stets ein leistungsstarker und kompetenter Partner für unsere Kunden im Raum Sachsen und Thüringen. Unser Aktionsradius erstreckt sich auf ca. 100 km im Umkreis.</p>
    <p>Mit unserem im Jahresdurchschnitt 15-köpfigem Team sind wir in der Lage, die meisten im Gerüstbau geforderten Leistungen zu erbringen. Einen Einblick über von uns ausgeführte Arbeiten erhalten Sie auf den nachfolgenden Seiten.</p>
    <p>Wir arbeiten ausschließlich mit Kornath-Gerüsten.<br>Dafür stehen uns ca. 40.000 m² Kornath-Flink-Gerüst, ca. 4.000 m² Modulgerüst, Kassetten- und Planendächer, Treppenaufgänge und Nottreppen, Fahr- und Rollgerüste sowie weitere Sonderteile zur Verfügung.</p>
    <p>Für den Transport des Gerüstmaterials haben wir vier LKW, z.T. mit Ladekran, und einen Transporter im Einsatz.</p>
    <p>Wir arbeiten ständig mit verschiedenen Bau- und Dachdeckerfirmen, Handwerksbetrieben, Ingenieurbüros, Kommunen, Kirchen, landwirtschaftlichen Betrieben, der Industrie und Privatpersonen zusammen.</p>
    <p>Für Ihre anstehenden Gerüstbauarbeiten sehen wir uns als zuverlässigen und flexiblen Partner, bitte kontaktieren Sie uns.</p>
  </div>
  <div class="abs history-photo" role="img" aria-label="Mit Planen verkleidetes Gerüst an einem Altstadthaus"></div>
</main>

<footer>
  <div class="abs footer-rule"></div>
  <div class="abs footer-col" style="left:72px;width:80px;line-height:2.1">Gerüstbau Wendrich GmbH</div>
  <div class="abs footer-col" style="left:169px">Am Kirchberg 7<br>09871 Talbrunn</div>
  <div class="abs footer-col" style="left:309px">Tel. 03799-410275<br>Fax. 03799-41029<br><span style="display:block;margin-top:8px">Datenschutz</span></div>
  <div class="abs footer-col" style="left:445px">© 2022 Gerüstbau Wendrich GmbH</div>
  <div class="abs badge"></div>
  <div class="abs footer-col" style="left:753px">Die Präqualifizierung erfolgte unter der<br>Registriernummer 120.004417</div>
  <div class="abs partner">
    <span class="pname">Kornath</span><span class="square"></span>
    <span class="claim">Wir bauen mit<br>Kornath-Gerüstsystemen</span>
  </div>
</footer>
</body>
</html>
```